Business card design for new, innovative company - BluePlinth

We are a new company looking for a business card design that is fun, different and quirky. Must use corporate colour green - CMYK C:55, M:0, Y:100, K:0, and corporate colour grey - C:0, M:0, Y: 0, K:70.

We have developed the first real time data application, in which people are able to profile the data of their existing customers in order to pull out more good fit clients to direct their marketing activities at.

Industry/Entity Type

Marketing

Requirements
Must have
• Logo, name, title, telephone number, fax number, email, website, address

```html
<!DOCTYPE html>
<html lang="en">
<head>
<meta charset="utf-8">
<title>BluePlinth business cards</title>
<link rel="stylesheet" href="https://fonts.googleapis.com/css2?family=Open+Sans:ital,wght@0,400;0,600;0,700;0,800;1,400&display=swap">
<style>
  :root {
    --brand-green: #7dc242;
    --brand-grey: #6d6e71;
    --card-white: #ffffff;
    --backdrop: #4a2e1f;
    --text-on-dark: #ffffff;
  }
  * { box-sizing: border-box; margin: 0; padding: 0; }
  html, body {
    width: 1200px; height: 734px; overflow: hidden;
    background: var(--backdrop);
    font-family: "Open Sans", Arial, sans-serif;
  }
  .stage { position: relative; width: 1200px; height: 734px; }
  .card {
    position: absolute; width: 470px; height: 296px;
    background: var(--card-white);
    box-shadow: 0 10px 24px rgba(0,0,0,0.45);
    overflow: hidden;
  }
  .card--front { left: 100px; top: 115px; }
  .card--back  { left: 630px; top: 320px; }
  .card__waves { position: absolute; inset: 0; width: 470px; height: 296px; }
  .wordmark {
    position: absolute; font-weight: 800; color: var(--brand-green);
    letter-spacing: -1.5px; line-height: 1;
  }
  .card--front .wordmark { left: 38px; top: 36px; font-size: 36px; }
  .card--back .wordmark { left: 46px; top: 60px; font-size: 44px; }
  .holder { position: absolute; left: 42px; top: 90px; }
  .holder__name { font-size: 17px; font-weight: 700; color: var(--brand-green); }
  .holder__title { font-size: 13px; font-style: italic; color: var(--brand-grey); margin-top: 2px; }
  .contact {
    position: absolute; right: 14px; top: 164px; list-style: none;
    color: var(--text-on-dark); font-size: 13.5px;
  }
  .contact__row {
    display: flex; justify-content: flex-end; align-items: center;
    height: 26px; gap: 10px; white-space: nowrap;
  }
  .contact__icon { width: 16px; height: 16px; flex: none; }
  .website {
    position: absolute; right: 34px; bottom: 30px;
    color: var(--text-on-dark); font-size: 16px; font-weight: 700;
  }
</style>
</head>
<body>
<main class="stage">

  <section class="card card--front" aria-label="Business card front">
    <svg class="card__waves" viewBox="0 0 470 296" aria-hidden="true">
      <path fill="var(--brand-green)" d="M0,158 L86,238 C200,172 330,108 470,80 L470,296 L0,296 Z"/>
      <path fill="var(--brand-grey)" d="M0,186 L86,252 C200,190 330,130 470,106 L470,296 L0,296 Z"/>
    </svg>
    <div class="wordmark">BluePlinth</div>
    <div class="holder">
      <p class="holder__name">Claire Dawson</p>
      <p class="holder__title">Managing Director</p>
    </div>
    <ul class="contact">
      <li class="contact__row">07700900482
        <svg class="contact__icon" viewBox="0 0 16 16" aria-hidden="true"><rect x="4" y="1" width="8" height="14" rx="1.5" fill="none" stroke="var(--brand-green)" stroke-width="1.6"/><rect x="5.5" y="3" width="5" height="7" fill="var(--brand-green)"/></svg>
      </li>
      <li class="contact__row">01632 960514
        <svg class="contact__icon" viewBox="0 0 16 16" aria-hidden="true"><path fill="var(--brand-green)" d="M3.5,1.5 L6,1 L7.5,4.5 L5.8,5.8 C6.6,7.6 8.4,9.4 10.2,10.2 L11.5,8.5 L15,10 L14.5,12.5 C14,14 12.5,15 11,14.6 C6.5,13.4 2.6,9.5 1.4,5 C1,3.5 2,2 3.5,1.5 Z"/></svg>
      </li>
      <li class="contact__row">claire.dawson@plinthdatagroup.com
        <svg class="contact__icon" viewBox="0 0 16 16" aria-hidden="true"><rect x="0.5" y="3" width="15" height="10" fill="var(--brand-green)"/><path d="M0.5,3 L8,9 L15.5,3" fill="none" stroke="var(--brand-grey)" stroke-width="1.2"/></svg>
      </li>
      <li class="contact__row">22a Fenway Court, Ely, Cambridgeshire, CB7 4XY
        <svg class="contact__icon" viewBox="0 0 16 16" aria-hidden="true"><path fill="var(--brand-green)" d="M8,0.5 C4.9,0.5 2.8,2.8 2.8,5.8 C2.8,9.5 8,15.5 8,15.5 C8,15.5 13.2,9.5 13.2,5.8 C13.2,2.8 11.1,0.5 8,0.5 Z"/><circle cx="8" cy="5.8" r="2" fill="var(--brand-grey)"/></svg>
      </li>
    </ul>
  </section>

  <section class="card card--back" aria-label="Business card back">
    <svg class="card__waves" viewBox="0 0 470 296" aria-hidden="true">
      <path fill="var(--brand-grey)" d="M0,168 L78,244 C200,178 330,112 470,90 L470,296 L0,296 Z"/>
      <path fill="var(--brand-green)" d="M0,192 L78,256 C200,194 330,130 470,110 L470,296 L0,296 Z"/>
    </svg>
    <div class="wordmark">BluePlinth</div>
    <p class="website">www.blueplinth.com</p>
  </section>

</main>
</body>
</html>
```